Cool payments solutions startup needs a brochure and product overview (Tov'ra)

We are a technology company that is working a platform to improve social inclusion in Latin America. Name Tovra means "work done for the good of the community" and we are targeting financial institutions and young profesionals (think lumeo or blue fox).

We need a brochure that would provide a brief overview of our platform and our services.

We prepared the illustration design that would describe the brochure, the rest is up to the designer to provide ideas.

We are a financial company focusing on financial inclusion.

Idea is to have a simple, minimalistic design. You can use sketch or handwriting to assist int he design.

Enclosed is the provided outline of the brochure with our sketched. It is necessary to provide illustrations from the sketched that are provided in the brochure.

Please keep in mind we don't have the final text (use generic text) and that we will translate all the text to several languages.

Main focus is digital distribution, not planning print for now. In case you will prepare print prep it will be two A4 pages (A5).

Ideas for design:
www.quarvin.org
http://plindo.com
http://wexombrit.io

Target Market(s)

technology companies and developers

Industry/Entity Type

Information Technology

Font styles to use
Serif
Sans Serif

Colors
00a990
33b8a4
88d0c7
9bcb3c
abd037
cadf82
eaf2ce
f8fcfc

Requirements
Must have
• Illustration as sketched in the attached documents.
• We are open for suggestions, but the basic elements must be matched.
Nice to have
• A complete 4 pages for a print (A4).
• We will distribute the brochure digitally.

```html
<!DOCTYPE html>
<html lang="en">
<head>
<meta charset="utf-8">
<title>Tovra – Brochure</title>
<link href="https://fonts.googleapis.com/css2?family=Montserrat:wght@300;400;600&display=swap" rel="stylesheet">
<style>
:root{
  --stage:#222222;
  --paper:#ffffff;
  --teal:#00a990;
  --teal-soft:#33b8a4;
  --teal-glow:#88d0c7;
  --lime:#9bcb3c;
  --ink:#555b5a;
  --rule:#cfd6d5;
}
*{margin:0;padding:0;box-sizing:border-box}
html,body{width:960px;height:1200px;overflow:hidden;background:var(--stage);font-family:"Montserrat",sans-serif}
.page{position:absolute;width:382px;height:494px;background:var(--paper);box-shadow:0 6px 18px rgba(0,0,0,.45);overflow:hidden;color:var(--teal)}
.page--cover{left:72px;top:71px}
.page--flow{left:514px;top:71px}
.page--features{left:72px;top:632px}
.page--contact{left:514px;top:632px}
.page__footer-stripe{position:absolute;left:0;right:0;bottom:0;height:4px;background:var(--teal)}
.center{position:absolute;left:0;right:0;text-align:center}
.brand{display:flex;justify-content:center;align-items:center;gap:12px;font-weight:400;font-size:34px;letter-spacing:9px;line-height:1;text-transform:uppercase}
.brand__dot{width:14px;height:14px;border-radius:50%;background:currentColor;flex:none}
.brand-sub{font-weight:400;font-size:10.5px;line-height:13px}
.band{position:absolute;left:0;right:0;background:var(--teal)}
.world-map{position:absolute;left:10px;right:10px;top:60px;height:160px;border-radius:50%;
  background:radial-gradient(ellipse at center,rgba(255,255,255,.55) 0%,rgba(136,208,199,.45) 40%,rgba(0,169,144,0) 72%)}
.tagline{font-weight:300;font-size:11.5px}
.flow-heading{font-weight:300;font-size:17px;line-height:19px}
.flow-intro{font-weight:300;font-size:7.3px;color:var(--ink)}
.flow-diagram{position:absolute;left:32px;top:125px;width:318px;height:261px}
.flow-note{font-weight:300;font-size:5.8px;line-height:8.5px;color:var(--ink);padding:0 36px}
.feature__icon{position:absolute;left:33px;width:28px;height:28px;fill:var(--teal)}
.feature__title{position:absolute;left:81px;font-weight:600;font-size:8.6px;letter-spacing:.4px;line-height:11px}
.feature__text{position:absolute;left:81px;right:34px;font-weight:300;font-size:6.2px;line-height:8.6px;color:var(--ink)}
.feature-rule{position:absolute;left:21px;right:22px;height:1px;background:var(--rule)}
.contact{color:#fff}
.contact__label{font-weight:300;font-size:11px;line-height:13px}
.contact__line{font-weight:300;font-size:9px;line-height:11px}
</style>
</head>
<body>
<svg width="0" height="0" style="position:absolute" aria-hidden="true">
  <symbol id="i-wallet" viewBox="0 0 24 24"><path d="M4 7l11-4 1 4z"/><rect x="2" y="7" width="19" height="14" rx="1.5"/><rect x="14" y="11" width="9" height="6" rx="1" fill="#fff"/><circle cx="17" cy="14" r="1.3"/></symbol>
  <symbol id="i-cashier" viewBox="0 0 24 24"><rect x="4" y="2" width="4" height="10"/><path d="M8 9h8l4 6H8z"/><rect x="2" y="15" width="20" height="7" rx="1"/></symbol>
  <symbol id="i-channel" viewBox="0 0 24 24"><path d="M3 10l14-7v18L3 14z"/><rect x="17" y="9" width="4" height="5" rx="1"/><path d="M6 14l2 7h3l-2-7z"/></symbol>
  <symbol id="i-gateway" viewBox="0 0 24 24"><path d="M6 19a5 5 0 0 1 0-10 7 7 0 0 1 13 1 4.5 4.5 0 0 1 0 9z"/><circle cx="12" cy="15" r="4.5" fill="#fff"/><path d="M12 12l-2.5 3h1.6v3h1.8v-3h1.6z"/></symbol>
  <symbol id="i-network" viewBox="0 0 24 24"><circle cx="12" cy="12" r="3.5"/><circle cx="12" cy="3" r="2"/><circle cx="12" cy="21" r="2"/><circle cx="3" cy="12" r="2"/><circle cx="21" cy="12" r="2"/><circle cx="5.5" cy="5.5" r="2"/><circle cx="18.5" cy="5.5" r="2"/><circle cx="5.5" cy="18.5" r="2"/><circle cx="18.5" cy="18.5" r="2"/><path d="M12 3v18M3 12h18M5.5 5.5l13 13M18.5 5.5l-13 13" stroke="currentColor" stroke-width="1"/></symbol>
  <symbol id="i-coins" viewBox="0 0 24 24"><ellipse cx="12" cy="19" rx="8" ry="3"/><ellipse cx="12" cy="14" rx="8" ry="3"/><ellipse cx="12" cy="9" rx="8" ry="3"/><ellipse cx="12" cy="5" rx="6" ry="3.5" fill="#fff"/><ellipse cx="12" cy="5" rx="4.5" ry="2.3"/></symbol>
  <symbol id="i-shield" viewBox="0 0 24 24"><path d="M12 1l9 3v7c0 6-4 10-9 12-5-2-9-6-9-12V4z"/><path d="M8 12l3 3 5-6" fill="none" stroke="#fff" stroke-width="2"/></symbol>
  <symbol id="i-person" viewBox="0 0 24 24"><circle cx="12" cy="7" r="5"/><path d="M3 23c0-6 4-9 9-9s9 3 9 9z"/></symbol>
  <symbol id="i-store" viewBox="0 0 24 24"><path d="M2 3h20v6H2z"/><rect x="4" y="9" width="16" height="13"/><rect x="9" y="13" width="6" height="9" fill="#9bcb3c"/></symbol>
  <symbol id="i-company" viewBox="0 0 24 24"><path d="M5 2h14v20H5z"/><path d="M8 5h2v2H8zM14 5h2v2h-2zM8 10h2v2H8zM14 10h2v2h-2zM8 15h2v2H8zM14 15h2v2h-2z" fill="#9bcb3c"/></symbol>
  <symbol id="i-laptop" viewBox="0 0 24 24"><rect x="3" y="3" width="18" height="13" rx="1"/><rect x="5" y="5" width="14" height="9" fill="#9bcb3c"/><path d="M1 17h22l-2 3H3z"/></symbol>
  <symbol id="i-mail" viewBox="0 0 24 24"><rect x="2" y="5" width="20" height="14"/><path d="M2 5l10 8 10-8" fill="none" stroke="#9bcb3c" stroke-width="1.5"/></symbol>
  <symbol id="i-globe" viewBox="0 0 24 24"><circle cx="12" cy="12" r="10" fill="none" stroke="#fff" stroke-width="2"/><ellipse cx="12" cy="12" rx="4" ry="10" fill="none" stroke="#fff" stroke-width="1.5"/><path d="M2 12h20M4 7h16M4 17h16" stroke="#fff" stroke-width="1.5"/></symbol>
  <symbol id="i-mobile" viewBox="0 0 24 24"><rect x="6" y="1" width="12" height="22" rx="2"/><rect x="8" y="4" width="8" height="14" fill="#9bcb3c"/></symbol>
  <symbol id="i-house" viewBox="0 0 24 24"><path d="M12 2L1 12h3v10h16V12h3z"/><rect x="10" y="15" width="4" height="7" fill="#9bcb3c"/></symbol>
  <symbol id="i-bank" viewBox="0 0 24 24"><path d="M12 1L2 7h20z"/><path d="M4 9h3v10H4zM10 9h4v10h-4zM17 9h3v10h-3zM2 20h20v3H2z"/></symbol>
  <symbol id="i-hands" viewBox="0 0 24 24"><path d="M1 9l5-3 5 3 4-3 8 4-4 6-6 4-6-3-4-4z"/></symbol>
  <symbol id="i-card" viewBox="0 0 24 24"><path d="M3 9l12-7 4 6-12 7z"/><rect x="3" y="12" width="18" height="10" rx="1"/><rect x="3" y="15" width="18" height="2" fill="#9bcb3c"/></symbol>
  <symbol id="i-mmoney" viewBox="0 0 24 24"><rect x="6" y="1" width="12" height="22" rx="2"/><rect x="8" y="4" width="8" height="14" fill="#9bcb3c"/><text x="12" y="15" font-size="9" text-anchor="middle" fill="#fff" font-family="Montserrat,sans-serif">$</text></symbol>
</svg>

<!-- Cover -->
<section class="page page--cover">
  <div class="center brand" style="top:44px"><span class="brand__dot"></span><span>Tovra</span></div>
  <div class="center brand-sub" style="top:90px">Public infrastructure for money</div>
  <div class="band" style="top:136px;height:275px">
    <div class="world-map" role="img" aria-label="Dotted world map linked by glowing arcs"></div>
  </div>
  <div class="center tagline" style="top:443px">Tov’ra – work for the good of the community.</div>
</section>

<!-- Flow -->
<section class="page page--flow">
  <div class="center flow-heading" style="top:32px">Money is only information about<br>what we owe each other.</div>
  <div class="center flow-intro" style="top:91px">2.5 billion people accross the world don’t have access to financial services.</div>
  <svg class="flow-diagram" viewBox="0 0 318 261" font-family="Montserrat,sans-serif" font-weight="300" font-size="6" fill="#fff" text-anchor="middle">
    <rect y="0" width="318" height="53" fill="#9bcb3c"/>
    <rect y="53" width="318" height="53" fill="#00a990"/>
    <rect y="106" width="318" height="53" fill="#9bcb3c"/>
    <rect y="159" width="318" height="53" fill="#00a990"/>
    <rect y="212" width="318" height="49" fill="#9bcb3c"/>
    <path d="M153 53h12l-6 8z" fill="#9bcb3c"/>
    <path d="M153 106h12l-6 8z" fill="#00a990"/>
    <path d="M153 159h12l-6 8z" fill="#9bcb3c"/>
    <path d="M153 212h12l-6 8z" fill="#00a990"/>

    <use href="#i-person" x="59" y="7" width="22" height="22"/><text x="70" y="39">Person</text>
    <use href="#i-store" x="118" y="7" width="22" height="22"/><text x="129" y="39">Store</text>
    <use href="#i-company" x="177" y="7" width="22" height="22"/><text x="188" y="39">Company</text>
    <use href="#i-laptop" x="237" y="7" width="22" height="22"/><text x="248" y="39">Web App</text>

    <use href="#i-wallet" x="90" y="60" width="24" height="24" style="fill:#fff"/><text x="102" y="92">Wallet</text>
    <text x="159" y="76">Pay/Receive</text>
    <use href="#i-cashier" x="207" y="60" width="24" height="24"/><text x="219" y="92">Cashier</text>

    <use href="#i-mail" x="47" y="116" width="22" height="22"/><text x="58" y="146">SMS</text>
    <use href="#i-globe" x="99" y="116" width="22" height="22"/><text x="110" y="146">Web</text>
    <text x="159" y="130">Using any</text><text x="159" y="138">Channels</text>
    <use href="#i-channel" x="199" y="116" width="22" height="22"/><text x="210" y="146">Voice</text>
    <use href="#i-mobile" x="251" y="116" width="22" height="22"/><text x="262" y="146">APP</text>

    <use href="#i-network" x="91" y="167" width="24" height="24" style="color:#fff"/><text x="103" y="200">Transaction</text>
    <text x="159" y="181">From any</text><text x="159" y="189">Currency</text><text x="159" y="197">or gateway</text>
    <use href="#i-gateway" x="203" y="167" width="24" height="24" style="fill:#fff"/><text x="215" y="200">Gateway</text>

    <use href="#i-house" x="17" y="221" width="22" height="22"/><text x="28" y="253">Agents</text>
    <use href="#i-bank" x="69" y="221" width="22" height="22"/><text x="80" y="253">Banks</text>
    <use href="#i-coins" x="121" y="221" width="22" height="22" style="fill:#fff"/><text x="132" y="253">Loyalty</text>
    <use href="#i-hands" x="171" y="221" width="22" height="22"/><text x="182" y="253">Credit Unions</text>
    <use href="#i-card" x="224" y="221" width="22" height="22"/><text x="235" y="253">Credit Card</text>
    <use href="#i-mmoney" x="273" y="221" width="22" height="22"/><text x="284" y="253">Mobile Money</text>
  </svg>
  <p class="center flow-note" style="top:428px">Lorem ipsum dolor sit amet, consectetuer adipiscing elit, sed diam nonummy nibh euismod tincidunt ut laoreet dolore magna aliquam erat volutpat. Ut wisi enim ad minim veniam, quis nostrud exerci tation ullamcorper suscipit lobortis nisl ut aliquip ex ea commodo consequat.</p>
  <div class="page__footer-stripe"></div>
</section>

<!-- Features -->
<section class="page page--features">
  <svg class="feature__icon" style="top:32px" viewBox="0 0 24 24"><use href="#i-wallet"/></svg>
  <div class="feature__title" style="top:32px">WALLET</div>
  <div class="feature__text" style="top:45px">Universal, omni-channel wallet that is accessible on any device. True one action payment making it as simple and accessible as cash.</div>
  <div class="feature-rule" style="top:72px"></div>

  <svg class="feature__icon" style="top:96px" viewBox="0 0 24 24"><use href="#i-cashier"/></svg>
  <div class="feature__title" style="top:98px">CAHIER</div>
  <div class="feature__text" style="top:111px">Universal interface for accepting any form payments. Personalized information and benefits program provide a contexts to what otherwise would be only</div>
  <div class="feature-rule" style="top:140px"></div>

  <svg class="feature__icon" style="top:162px" viewBox="0 0 24 24"><use href="#i-channel"/></svg>
  <div class="feature__title" style="top:164px">CHANNEL</div>
  <div class="feature__text" style="top:177px">Text message, voice call, ussd, web or app. Any channel you prefer to use. Powered by Relaycast – 4 billion transactions per month, 190 countries, 800+ operators.</div>
  <div class="feature-rule" style="top:208px"></div>

  <svg class="feature__icon" style="top:228px" viewBox="0 0 24 24"><use href="#i-gateway"/></svg>
  <div class="feature__title" style="top:230px">GATEWAYS</div>
  <div class="feature__text" style="top:243px">Gateways are issuing entitites that that people trust to hold their deposit and issue credits into the network. Tov’ra network connects the different gateways</div>
  <div class="feature-rule" style="top:274px"></div>

  <svg class="feature__icon" style="top:291px;color:var(--teal)" viewBox="0 0 24 24"><use href="#i-network"/></svg>
  <div class="feature__title" style="top:293px">TRANSACTIONS</div>
  <div class="feature__text" style="top:306px">Tov’ra uses a global edger to keep track of all the balances and transactions for every single account on the network. Tov’ra ensures that all transactions are valid and get applied</div>
  <div class="feature-rule" style="top:340px"></div>

  <svg class="feature__icon" style="top:357px" viewBox="0 0 24 24"><use href="#i-coins"/></svg>
  <div class="feature__title" style="top:359px">CURRENCY</div>
  <div class="feature__text" style="top:372px">Tov’ra can allow to send any currency between any address in the system trough its builtLin exchange. Pells is the universal, bridge currency used to settle dollars, yens, pesos, loytalty points, giftcards or bitcoins</div>
  <div class="feature-rule" style="top:408px"></div>

  <svg class="feature__icon" style="top:424px" viewBox="0 0 24 24"><use href="#i-shield"/></svg>
  <div class="feature__title" style="top:424px">ADDRESS</div>
  <div class="feature__text" style="top:437px">Each unique Tov’ra address can be referenced by something we all know- your phone number. Two factor authentication and global ledger ensure a secure, fraud free system.</div>
  <div class="page__footer-stripe"></div>
</section>

<!-- Contact -->
<section class="page page--contact">
  <div class="band contact" style="top:136px;height:274px">
    <div class="center brand" style="top:56px"><span class="brand__dot"></span><span>Tovra</span></div>
    <div class="center brand-sub" style="top:103px">Public infrastructure for money</div>
    <div class="center contact__label" style="top:151px">Contact</div>
    <div class="center contact__line" style="top:174px">418 Calloway Lane Northwest<br>Brenford, BR 40917</div>
    <div class="center contact__line" style="top:216px">(555) 014-2290</div>
    <div class="center contact__line" style="top:237px">info@tovra.com</div>
    <div class="center contact__line" style="top:258px">www.tovra.com</div>
  </div>
</section>
</body>
</html>
```